Brightoak Business Card

Professional Business Card Design required using the attached contact information.

Contact information can be rearranged as required.

The company is a new start up venture developing solar systems, the branding should be in keeping with that of one of the investors whose website is as follows https://www.corvellan.com/

```html
<!DOCTYPE html>
<html lang="en">
<head>
<meta charset="utf-8">
<title>Brightoak Business Card</title>
<link href="https://fonts.googleapis.com/css2?family=Michroma&family=Roboto+Condensed:wght@300;400&display=swap" rel="stylesheet">
<style>
  :root {
    --stage: #e6e7e6;
    --brand-green: #2a6653;
    --deep-green: #1f4f40;
    --paper: #ffffff;
    --rule-blue: #7fb3c9;
    --ink-grey: #6f6f6f;
  }
  * { margin: 0; padding: 0; box-sizing: border-box; }
  html, body { width: 1200px; height: 965px; overflow: hidden; }
  body {
    background: var(--stage);
    font-family: "Roboto Condensed", sans-serif;
    display: flex; flex-direction: column; align-items: center; justify-content: center; gap: 48px;
  }
  .card {
    width: 660px; height: 377px; position: relative;
    box-shadow: 0 6px 18px rgba(0,0,0,.18);
  }
  .card-back {
    background: var(--brand-green);
    display: flex; align-items: center; justify-content: center; gap: 18px;
  }
  .card-back .mark-dot { width: 34px; height: 34px; border-radius: 50%; background: var(--paper); }
  .card-back .mark-name {
    font-family: "Roboto Condensed", sans-serif; font-weight: 300;
    font-size: 54px; color: var(--paper); letter-spacing: 1px;
  }
  .card-front { background: var(--paper); }
  .logo {
    position: absolute; left: 70px; top: 150px;
    display: flex; align-items: center; gap: 12px;
  }
  .logo .mark-dot { width: 22px; height: 22px; border-radius: 50%; background: var(--brand-green); }
  .logo .mark-name { font-weight: 300; font-size: 38px; color: var(--brand-green); }
  .divider {
    position: absolute; left: 318px; top: 110px; width: 1.5px; height: 140px;
    background: var(--rule-blue);
  }
  .details { position: absolute; left: 340px; top: 100px; }
  .person-name {
    font-family: "Michroma", sans-serif; font-size: 19px; color: var(--brand-green);
    letter-spacing: 1px; margin-bottom: 12px;
  }
  .contact-list { list-style: none; }
  .contact-list li {
    display: flex; align-items: center; gap: 9px;
    font-weight: 300; font-size: 15px; color: var(--ink-grey); line-height: 21px;
  }
  .contact-list svg { width: 14px; height: 14px; flex: none; }
  .company-caps {
    font-family: "Michroma", sans-serif; font-size: 14px; color: var(--brand-green);
    letter-spacing: .8px; margin-top: 20px;
  }
  .company-line {
    position: absolute; left: 200px; bottom: 36px;
    font-weight: 300; font-size: 28px; color: var(--brand-green);
  }
</style>
</head>
<body>
  <section class="card card-back">
    <span class="mark-dot"></span>
    <span class="mark-name">Brightoak</span>
  </section>

  <section class="card card-front">
    <div class="logo">
      <span class="mark-dot"></span>
      <span class="mark-name">Brightoak</span>
    </div>
    <div class="divider"></div>
    <div class="details">
      <h1 class="person-name">DANIEL HALE</h1>
      <ul class="contact-list">
        <li>
          <svg viewBox="0 0 16 16" fill="none" stroke="#2a6653" stroke-width="1.4"><path d="M3 2h3l1.5 3.5-2 1.2a9 9 0 0 0 3.8 3.8l1.2-2L14 10v3a1 1 0 0 1-1 1A11 11 0 0 1 2 3a1 1 0 0 1 1-1z"/></svg>
          +1 (555) 240-7316
        </li>
        <li>
          <svg viewBox="0 0 16 16" fill="none" stroke="#2a6653" stroke-width="1.4"><rect x="1.5" y="3.5" width="13" height="9"/><path d="M1.5 3.5l6.5 5 6.5-5"/></svg>
          daniel.hale@brightoak-renewables.com
        </li>
        <li>
          <svg viewBox="0 0 16 16" fill="#2a6653"><path d="M8 1a5 5 0 0 0-5 5c0 3.8 5 9 5 9s5-5.2 5-9a5 5 0 0 0-5-5zm0 7a2 2 0 1 1 0-4 2 2 0 0 1 0 4z"/></svg>
          218 Harbor Street, Boston, MA 02110
        </li>
      </ul>
      <p class="company-caps">BRIGHTOAK RENEWABLES LLC</p>
    </div>
    <p class="company-line">Brightoak Renewables LLC</p>
  </section>
</body>
</html>
```